First of a series of workplace posters- our values statement

To produce a high quality poster of our values, we would like one in a3 and one in a4 both full colour
By utilising the supplied text , the intent is to produce a really striking poster for all our work places, which set out our company values. we are looking for really strong graphical elements which support the message visually . This will be the first of a series of posters, so we are looking to establish at stylistic theme for all with this one. for more on our business,

Target Market(s)

Internal and external audiences, our clients are all tier one companies

Requirements
Must have
• contemporary design rather than conservative, visually striking
• Must be clearly readable from a reasonable distance
Nice to have
• would be nice to tie in to the blue and greens of our logo in similar fashion to our website. www.qrtbuildwise.com
Should not have
• Difficult to read fonts,

```html
<!DOCTYPE html>
<html lang="en">
<head>
<meta charset="utf-8">
<title>Our Values Poster</title>
<link rel="stylesheet" href="https://fonts.googleapis.com/css2?family=Roboto:wght@900&family=Roboto+Condensed:wght@500;700&family=Montserrat:wght@400;700&display=swap">
<style>
  :root {
    --navy: #1d4a80;
    --green: #6cb41e;
    --ink: #3a3a3a;
    --card-top: #ffffff;
    --card-bottom: #e6e7e8;
    --spine: #4a4a4a;
    --dark-band: #2b2b2c;
    --backdrop: #b5b5b5;
  }
  * { margin: 0; padding: 0; box-sizing: border-box; }
  html, body { width: 703px; height: 1200px; overflow: hidden; }
  body { background: var(--backdrop); position: relative; }

  .poster {
    position: absolute; left: 32px; top: 147px;
    width: 498px; height: 704px;
    background: #fff; overflow: hidden;
    transform: scale(1.285); transform-origin: top left;
    box-shadow: 4px 6px 10px rgba(0,0,0,.25);
    font-family: "Montserrat", sans-serif; color: var(--ink);
  }
  .poster-title {
    position: absolute; top: 24px; width: 100%; text-align: center;
    font-family: "Roboto", sans-serif; font-weight: 900;
    font-size: 40px; letter-spacing: 0.5px; color: var(--navy);
  }
  .spine { position: absolute; left: 248px; top: 100px; width: 1.2px; height: 560px; background: var(--spine); }
  .connector { position: absolute; height: 1px; background: var(--spine); width: 20px; }
  .connector.left { left: 229px; }
  .connector.right { left: 249px; width: 24px; }

  .value-card { position: absolute; width: 208px; }
  .value-card.left { left: 21px; text-align: right; }
  .value-card.right { left: 273px; text-align: left; }
  .card-header {
    height: 18px; line-height: 18px; padding: 0 12px;
    font-family: "Roboto Condensed", sans-serif; font-weight: 500;
    font-size: 7.6px; color: #fff; text-transform: uppercase;
    border-radius: 2px 14px 0 2px;
  }
  .card-header.green { background: var(--green); }
  .card-header.navy { background: var(--navy); }
  .card-body {
    padding: 6px 12px 8px; font-size: 5.4px; line-height: 1.45;
    background: linear-gradient(var(--card-top), var(--card-bottom));
    border-radius: 0 0 7px 7px;
    box-shadow: 0 2px 3px rgba(0,0,0,.18);
  }
  .lead { font-weight: 700; font-size: 6px; margin: 2px 0 5px; text-transform: uppercase; }
  .card-body p { margin-bottom: 5px; }
  .points { list-style: none; }
  .points li { margin-bottom: 3.6px; position: relative; }
  .left .points li { padding-right: 8px; }
  .right .points li { padding-left: 8px; }
  .points li::before {
    content: ""; position: absolute; top: 0.5px; width: 4.6px; height: 4.6px;
    border-radius: 50%; background: var(--green);
  }
  .points li::after {
    content: ""; position: absolute; top: 1.4px; width: 1.2px; height: 2px;
    border: solid #fff; border-width: 0 0.7px 0.7px 0; transform: rotate(40deg);
  }
  .left .points li::before { right: 0; }
  .left .points li::after { right: 1.8px; }
  .right .points li::before { left: 0; }
  .right .points li::after { left: 1.8px; }

  .base-band {
    position: absolute; left: 0; top: 650px; width: 280px; height: 54px;
    background: var(--dark-band);
  }
  .brand-ring { position: absolute; left: 0; top: 0; }
  .brand-name {
    position: absolute; left: 330px; top: 636px; width: 160px; text-align: center;
    font-family: "Montserrat", sans-serif; font-weight: 700;
    font-size: 17px; color: var(--navy);
  }
</style>
</head>
<body>
  <main class="poster">
    <h1 class="poster-title">OUR VALUES</h1>

    <div class="spine"></div>
    <div class="connector left" style="top:165px"></div>
    <div class="connector left" style="top:308px"></div>
    <div class="connector left" style="top:440px"></div>
    <div class="connector left" style="top:578px"></div>
    <div class="connector right" style="top:200px"></div>
    <div class="connector right" style="top:368px"></div>
    <div class="connector right" style="top:478px"></div>

    <section class="value-card left" style="top:88px">
      <h2 class="card-header green">We value our people above everything else</h2>
      <div class="card-body">
        <div class="lead">We demonstrate this by:</div>
        <ul class="points">
          <li>Providing safe, positive, enjoyable workplaces where everyone feels valued and respected</li>
          <li>Providing careers, not jobs, we grow together</li>
          <li>Encouraging inclusion, participation and collaboration.</li>
          <li>Recognising and rewarding contribution and excellence</li>
          <li>Supporting our people through tough times.</li>
          <li>Fostering healthy work life balance.</li>
        </ul>
      </div>
    </section>

    <section class="value-card left" style="top:241px">
      <h2 class="card-header navy">We value our people above everything else</h2>
      <div class="card-body">
        <div class="lead">We demonstrate this by:</div>
        <ul class="points">
          <li>Providing safe, positive, enjoyable workplaces where everyone feels valued and respected.</li>
          <li>Providing careers, not jobs, we grow together.</li>
          <li>Encouraging inclusion, participation and collaboration.</li>
          <li>Recognising and rewarding contribution and excellence.</li>
          <li>Supporting our people through tough times.</li>
          <li>Fostering healthy work life balance.</li>
        </ul>
      </div>
    </section>

    <section class="value-card left" style="top:384px">
      <h2 class="card-header green">We are proud of who we are</h2>
      <div class="card-body">
        <div class="lead">Our reputation means the world to us.<br>We:</div>
        <ul class="points">
          <li>Treat everyone with respect, and we expect it in return.</li>
          <li>Follow the rules. &nbsp;&nbsp; Do what we say we will do.</li>
          <li>Own our mistakes and we fix them.</li>
          <li>Are trustworthy and transparent.</li>
        </ul>
      </div>
    </section>

    <section class="value-card left" style="top:518px">
      <h2 class="card-header navy">We succeed together</h2>
      <div class="card-body">
        <p>We believe in win-win relationships. When our Business is profitable everyone benefits, our shareholders, employees, clients, suppliers and the community</p>
        <div class="lead">At QRT we:</div>
        <ul class="points">
          <li>work as a team, we get it done together</li>
          <li>are building on our success and growing together</li>
          <li>choose to work with employees, customers, and suppliers who fit our values.</li>
        </ul>
      </div>
    </section>

    <section class="value-card right" style="top:110px">
      <h2 class="card-header green">All our workplaces are safe work places</h2>
      <div class="card-body">
        <p>There is nothing more important to us than our team members going home healthy and safe every day, we won't accept anything less. We believe workplace safety is a management choice, by providing safe work systems and education we achieve our daily goal of Zero Harm.</p>
        <div class="lead">We:</div>
        <ul class="points">
          <li>Take the time to make our work areas safe, whatever it takes.</li>
          <li>Don't accept shortcuts. &nbsp;&nbsp;&nbsp; Look out for each other.</li>
          <li>Investigate our incidents and learn from them, no repeats.</li>
          <li>Are constantly looking for ways to improve the safety of our workplaces and the health of our team members.</li>
          <li>Think safe, work safe, go home safe!</li>
        </ul>
      </div>
    </section>

    <section class="value-card right" style="top:310px">
      <h2 class="card-header navy">The planet benefits from our existence</h2>
      <div class="card-body">
        <p>We are relentlessly pursuing our objective of providing our clients with pathways to sustainable development. To achieve our vision we</p>
        <ul class="points">
          <li>Minimise our environmental impact in everything we do.</li>
          <li>Actively develop and promote world's best practices in rehabilitation of disturbed land.</li>
        </ul>
      </div>
    </section>

    <section class="value-card right" style="top:429px">
      <h2 class="card-header green">We set the standard</h2>
      <div class="card-body" style="padding-top:10px; padding-bottom:14px">
        <ul class="points">
          <li>We are uncompromising on quality.</li>
          <li>We are the best at what we do, and we do what we are best at.</li>
          <li>We are always improving.</li>
        </ul>
      </div>
    </section>

    <div class="base-band"></div>
    <svg class="brand-ring" width="498" height="704" viewBox="0 0 498 704" aria-hidden="true">
      <circle cx="410" cy="662" r="132" fill="var(--navy)"/>
      <circle cx="410" cy="662" r="98" fill="#fff"/>
    </svg>
    <div class="brand-name">QRT Buildwise</div>
  </main>
</body>
</html>
```